Sports / Entertainment Media Co needs a biz card design

We are a media co / luxury lifestyle brand that targets professional athletes, entertainers and high net-worth fans. We are currently preparing for a relaunch and in need for new biz cards. I envision a black on black card with a pop of color on opposite side. Color Palette black, white, red etc. I want this card to exude sexiness and power. Very high stylized, hip and cool. I have attached the logo - I would like to see it all in black, but also open to other ideas. I will also upload a current card with all information needed on this new card. Furthermore I will add some samples of other cards I love. Thanks!!!

I provided suggestions, however I am open to all ideas!!   Be as creative as you can.  Think cutting-edge, sexy and powerful.  Take a look at the cards I uploaded to get a sense for what I like.  Thanks!!!

Entertainment

```html
<!DOCTYPE html>
<html lang="en">
<head>
<meta charset="utf-8">
<title>Stride Media Ventures – Business Card</title>
<link rel="stylesheet" href="https://fonts.googleapis.com/css2?family=Source+Sans+3:wght@400;600;700;800&display=swap">
<style>
  :root {
    --bg-light: #f2f3f4;
    --bg-dark: #c9cacc;
    --card: #333237;
    --band: #000000;
    --ink: #0c0c0d;
    --muted: #a9a9ad;
    --soft: #c2c2c6;
    --accent: #e3121b;
    --white: #ffffff;
    --domain: #8d8f93;
  }
  * { margin: 0; padding: 0; box-sizing: border-box; }
  html, body { width: 1200px; height: 1200px; overflow: hidden; }
  body {
    position: relative;
    background: radial-gradient(circle at 50% 48%, var(--bg-light) 0%, var(--bg-light) 35%, var(--bg-dark) 100%);
    font-family: "Source Sans 3", "Helvetica Neue", Arial, sans-serif;
  }

  .card {
    position: absolute;
    left: 228px;
    width: 744px;
    height: 422px;
    background: var(--card);
    overflow: hidden;
  }
  .card--front { top: 160px; border-radius: 34px 0 34px 0; }
  .card--back  { top: 590px; border-radius: 0 34px 0 34px; }

  /* Front */
  .front-edge-bar {
    position: absolute; left: 707px; top: 114px;
    width: 37px; height: 198px; background: var(--band);
  }
  .brand-vertical {
    position: absolute; left: 78px; top: 42px;
    writing-mode: vertical-rl;
    display: flex; align-items: center; gap: 14px;
  }
  .brand-vertical .brand-name {
    font-size: 88px; font-weight: 800; color: var(--ink);
    line-height: 1; letter-spacing: -2px;
  }
  .brand-dot { width: 28px; height: 28px; border-radius: 50%; background: var(--accent); }
  .brand-vertical-domain {
    position: absolute; left: 42px; top: 44px;
    writing-mode: vertical-rl;
    font-size: 17px; font-weight: 700; color: var(--domain); letter-spacing: 0.3px;
  }

  .holder { position: absolute; right: 78px; top: 36px; text-align: right; }
  .holder-name { font-size: 21px; font-weight: 700; color: var(--muted); letter-spacing: 0.4px; line-height: 1.15; }
  .holder-title { font-size: 19px; font-weight: 700; color: var(--ink); line-height: 1.15; }

  .company {
    position: absolute; right: 78px; top: 188px;
    font-size: 25px; font-weight: 700; color: var(--ink); letter-spacing: 0.3px;
  }

  .contacts {
    position: absolute; top: 328px; left: 249px;
    display: flex; gap: 18px;
    font-size: 17px; color: var(--soft); line-height: 23.5px;
  }
  .contact-list { list-style: none; }
  .contact-list li { display: flex; align-items: center; gap: 8px; }
  .contact-list li.indent { padding-left: 26px; }
  .icon { width: 18px; height: 18px; flex: none; }

  /* Back */
  .back-band {
    position: absolute; left: 0; top: 118px; width: 100%; height: 180px;
    background: var(--band);
  }
  .brand-wordmark {
    position: absolute; left: 86px; top: 0;
    display: flex; align-items: center; gap: 18px; height: 150px;
  }
  .brand-wordmark .brand-name {
    font-size: 150px; font-weight: 800; color: var(--white);
    line-height: 1; letter-spacing: -4px;
  }
  .brand-wordmark .brand-dot { width: 44px; height: 44px; margin-top: 38px; }
  .brand-domain {
    position: absolute; left: 92px; top: 142px;
    font-size: 20px; font-weight: 700; color: var(--domain);
  }
</style>
</head>
<body>

<section class="card card--front" aria-label="Card front">
  <div class="brand-vertical">
    <span class="brand-name">stride</span>
    <span class="brand-dot"></span>
  </div>
  <div class="brand-vertical-domain">stridemag.com</div>

  <div class="holder">
    <p class="holder-name">DANA MARLOWE</p>
    <p class="holder-title">President</p>
  </div>

  <p class="company">STRIDE MEDIA VENTURES LLC</p>

  <div class="front-edge-bar"></div>

  <div class="contacts">
    <ul class="contact-list">
      <li>
        <svg class="icon" viewBox="0 0 18 18" aria-hidden="true"><circle cx="9" cy="9" r="9" fill="var(--accent)"/><path d="M5 7.5c1.5-2.5 6.5-2.5 8 0l-1.5 1.2-1.4-1H7.9l-1.4 1z" fill="#1a1a1a"/></svg>
        305 555 0142
      </li>
      <li>
        <svg class="icon" viewBox="0 0 18 18" aria-hidden="true"><circle cx="9" cy="9" r="9" fill="var(--accent)"/><rect x="6" y="3.5" width="6" height="11" rx="1" fill="#1a1a1a"/><rect x="7" y="5" width="4" height="6" fill="var(--accent)"/></svg>
        954 555 0187
      </li>
      <li>
        <svg class="icon" viewBox="0 0 18 18" aria-hidden="true"><circle cx="9" cy="9" r="9" fill="var(--accent)"/><rect x="6" y="4" width="6" height="4" fill="#1a1a1a"/><rect x="4" y="8" width="10" height="5" rx="1" fill="#1a1a1a"/></svg>
        305 555 0119
      </li>
    </ul>
    <ul class="contact-list">
      <li>
        <svg class="icon" viewBox="0 0 18 18" aria-hidden="true"><circle cx="9" cy="9" r="9" fill="var(--accent)"/><rect x="4.5" y="5.5" width="9" height="7" fill="#1a1a1a"/><path d="M4.5 5.5l4.5 4 4.5-4" fill="none" stroke="var(--accent)" stroke-width="1"/></svg>
        dana@stridemag.com
      </li>
      <li>
        <svg class="icon" viewBox="0 0 18 18" aria-hidden="true"><circle cx="9" cy="9" r="9" fill="var(--accent)"/><path d="M9 3.5l5.5 5h-1.5V14H5V8.5H3.5z" fill="#1a1a1a"/></svg>
        2470 NE Harbor Drive, Ste 410
      </li>
      <li class="indent">Miami, FL 33137</li>
    </ul>
  </div>
</section>

<section class="card card--back" aria-label="Card back">
  <div class="back-band">
    <div class="brand-wordmark">
      <span class="brand-name">stride</span>
      <span class="brand-dot"></span>
    </div>
    <p class="brand-domain">stridemag.com</p>
  </div>
</section>

</body>
</html>
```